Sports Therapy Company Package Design for Kinesiology Tape

We are a high quality product company looking to stand out from the crowd. We produce a product called Velmora or Kinesiology Tape. The difference in our product offering is in quality. Our material is softer, stretches more, and more comfortable than other similar products.
The box design is rather small, it holds the Velmora Tape which is a little larger than a roll of hockey tape. We are looking for clean, high value looking design.
Our product helps people feel better and we look forward to a design to represent that concept.
We have attached the package design template and a word document with additional specifications of words to potentially use in your design, including our company name and product features.
Reason: Give more time to work on designs
Reason: Time for finishing design changes
Target Market(s)
Adults male and female who are active in sports. Athletes who suffer injury.
Industry/Entity Type
It Company
Look and feel
Each slider illustrates characteristics of the customer's brand and the style your logo design should communicate.

```html
<!DOCTYPE html>
<html lang="en">
<head>
<meta charset="utf-8">
<title>Velmora Tape – Package</title>
<link rel="stylesheet" href="https://fonts.googleapis.com/css2?family=Roboto+Condensed:wght@400;700;800&display=swap">
<style>
  :root {
    --bg-light: #f4f4f5;
    --bg-mid: #dcdcde;
    --box-black: #050505;
    --lime: #8dc63f;
    --lime-tab: #8cc441;
    --white: #ffffff;
    --photo-skin: #d9b7a3;
    --photo-pink: #e0578f;
    --photo-dark: #1c1c1c;
  }
  * { box-sizing: border-box; margin: 0; padding: 0; }
  html, body { width: 1200px; height: 1000px; overflow: hidden; }
  body {
    background: radial-gradient(ellipse at 50% 45%, var(--bg-light) 0%, var(--bg-mid) 100%);
    font-family: "Roboto Condensed", Arial, sans-serif;
    position: relative;
  }
  .package { position: absolute; left: 230px; top: 190px; width: 740px; height: 600px; }

  .hang-tab {
    position: absolute; left: 0; top: 0; width: 300px; height: 140px;
    background: var(--lime-tab);
  }
  .hang-slot {
    position: absolute; left: 86px; top: 52px; width: 128px; height: 36px;
    background: var(--bg-light); border-radius: 18px;
  }
  .hang-slot::before {
    content: ""; position: absolute; left: 52px; top: -10px;
    width: 24px; height: 24px; border-radius: 50%; background: var(--bg-light);
  }

  .panel { position: absolute; top: 140px; height: 460px; background: var(--box-black); color: var(--white); overflow: hidden; }
  .side-panel { left: 0; width: 300px; }
  .front-panel { left: 300px; width: 440px; border-left: 1px solid #1a1a1a; }

  .brand { display: flex; align-items: center; gap: 8px; font-weight: 700; font-size: 20px; color: var(--white); letter-spacing: 0.5px; }
  .brand-mark { width: 10px; height: 10px; background: var(--lime); }
  .side-panel .brand { position: absolute; left: 20px; top: 56px; }
  .front-panel .brand { position: absolute; left: 34px; top: 36px; font-size: 22px; }

  .usage-strip { position: absolute; left: 0; top: 94px; width: 300px; height: 168px; }

  .size { position: absolute; left: 20px; top: 292px; font-size: 32px; font-weight: 700; }
  .features { position: absolute; left: 20px; top: 342px; list-style: none; font-size: 13px; line-height: 21px; letter-spacing: 0.2px; }
  .features .lime { color: var(--lime); }
  .features .sep { color: var(--white); }

  .athlete-photo { position: absolute; left: 100px; top: 0; width: 240px; height: 460px; }

  .product-name { position: absolute; left: 30px; top: 246px; font-weight: 800; line-height: 0.92; }
  .product-name .line-brand { display: block; font-size: 92px; color: var(--white); letter-spacing: 1px; }
  .product-name .line-tape { display: block; font-size: 66px; color: var(--lime); margin-top: 4px; }
  .claims { position: absolute; left: 230px; top: 340px; font-size: 17px; line-height: 20px; }
  .claims .claim-soft { color: var(--lime); display: block; }
  .claims .claim-comfort { color: var(--white); display: block; }
</style>
</head>
<body>
  <div class="package">
    <div class="hang-tab"><span class="hang-slot"></span></div>

    <section class="panel side-panel">
      <div class="brand"><span class="brand-mark"></span>TERVIK</div>

      <svg class="usage-strip" viewBox="0 0 300 168" role="img" aria-label="Photos of coloured tape applied to a knee and a shoulder">
        <defs>
          <linearGradient id="knee" x1="0" y1="0" x2="1" y2="1">
            <stop offset="0" stop-color="var(--photo-dark)"/>
            <stop offset="0.5" stop-color="var(--photo-pink)"/>
            <stop offset="1" stop-color="var(--photo-skin)"/>
          </linearGradient>
          <linearGradient id="shoulder" x1="0" y1="0" x2="1" y2="1">
            <stop offset="0" stop-color="var(--photo-skin)"/>
            <stop offset="0.55" stop-color="var(--photo-pink)"/>
            <stop offset="1" stop-color="var(--photo-dark)"/>
          </linearGradient>
        </defs>
        <rect width="300" height="168" fill="#ffffff"/>
        <polygon points="0,0 118,0 72,168 0,168" fill="url(#knee)"/>
        <polygon points="132,0 300,0 300,0 258,168 86,168" fill="url(#shoulder)"/>
        <line x1="125" y1="0" x2="79" y2="168" stroke="var(--lime)" stroke-width="5"/>
        <line x1="306" y1="0" x2="262" y2="168" stroke="var(--lime)" stroke-width="5"/>
      </svg>

      <div class="size">5cm x 5m</div>
      <ul class="features">
        <li><span class="lime">100% NYLON TAPE</span> <span class="sep">/</span> <span class="lime">HYPOALLERGENIC</span></li>
        <li><span class="lime">200% ELASTICITY</span> <span class="sep">/</span> <span class="lime">ACRYLIC GLUE</span></li>
        <li><span class="lime">BETTER THAN KINETIC TAPE</span> <span class="sep">/</span> <span class="lime">NO DEGUMMING</span></li>
        <li><span class="lime">FAR MORE COMFORTABLE</span> <span class="sep">/</span> <span class="lime">WATER PROOF</span></li>
        <li><span class="lime">SMOOTH AND SOFT</span></li>
      </ul>
    </section>

    <section class="panel front-panel">
      <svg class="athlete-photo" viewBox="0 0 240 460" role="img" aria-label="Photo of a female athlete running toward the viewer">
        <defs>
          <radialGradient id="athlete" cx="0.5" cy="0.4" r="0.55">
            <stop offset="0" stop-color="#4a4a4a"/>
            <stop offset="0.6" stop-color="#1e1e1e"/>
            <stop offset="1" stop-color="var(--box-black)"/>
          </radialGradient>
        </defs>
        <rect width="240" height="460" fill="url(#athlete)"/>
      </svg>

      <div class="brand"><span class="brand-mark"></span>TERVIK</div>

      <h1 class="product-name">
        <span class="line-brand">VELMORA</span>
        <span class="line-tape">TAPE</span>
      </h1>
      <p class="claims">
        <span class="claim-soft">SMOOTH &amp; SOFT</span>
        <span class="claim-comfort">MORE COMFORTABLE</span>
      </p>
    </section>
  </div>
</body>
</html>
```